THE ORCHARD BELOW book cover needed

Hello friends! I'm working toward self-publishing my first novel in the next few months, and I'm looking to have a professional-looking, 6 in x 9 in cover to go along with the ebook release. I’m not looking for much, but the key is that it must look professional. I don’t want decorative fonts, but I also don’t want it to just look like Helvetica or Times New Roman.The text for the cover should be:A TIME FOR GREATNESSKARLIS WILDEI have attached a few images to show you where my head is at. I created a book cover myself on paint that looks horribly amateur, but it draws inspiration from a HPM campaign poster(also attached) where the title of the novel comes from. If you can make that same kind of cover, but make it look professional, that would be amazing! If you have other, simple ideas, I am also very, very open.Attached as well are a couple of simple, recent book covers that I like. That is the kind of thing that I am looking for.If this goes well, I may do a paperback release. In that case, I may need to contact you again for an additional fee to create the rest of the wraparound design. In addition, the book is the first in a projected trilogy, so there may be opportunities for you in the future for sequel covers.About the book: THE ORCHARD BELOW is a gripping, standalone thriller with an exciting take on history, relationships, conspiracy theories, and the current, volatile political state of America. In the present day, new information surrounding the 1963 assassination of Harold P. Merrow comes to light and Teodor Vasquelle, a young, best-selling journalist still reconciling his success with his dark past, finds himself more personally connected than he ever could have expected. But the story becomes something even bigger when an assassination attempt on the current demagogic president sends the whole world of journalism into a scramble, and Teodor finds himself confronted by an extremely difficult question: Is democracy real, or has it been an illusion fostered by these secretive ‘Wardens of the Ledger’ since 1776? Travelling across Syria, Canada, and the United States of America, the story becomes more unbelievable—and more personal—as increasingly prominent figures begin to enter Teodor’s orbit, intent on keeping their secrets safe by whatever means necessary.

Colors

Designer to choose colors to be used in the design.

Requirements
Must have
• Text
• Simplicity
• Professional look
Should not have
• Cheap fonts
• Complicated images

```html
<!DOCTYPE html>
<html lang="en">
<head>
<meta charset="utf-8">
<title>The Orchard Below — Brenno Saltvik</title>
<link rel="stylesheet" href="https://fonts.googleapis.com/css2?family=Bebas+Neue&display=swap">
<style>
  :root {
    --band-red: #c23a2e;
    --band-red-deep: #8c2a22;
    --band-white: #ffffff;
    --band-blue: #3a56a4;
    --band-blue-deep: #27397a;
    --title-red: #a52f29;
    --title-blue: #2e4786;
    --star: #ffffff;
    --author: #f4f1ec;
  }
  * { margin: 0; padding: 0; box-sizing: border-box; }
  html, body { width: 751px; height: 1200px; overflow: hidden; background: var(--band-white); }
  .cover {
    position: relative;
    width: 751px;
    height: 1200px;
    overflow: hidden;
  }
  .band { position: absolute; left: 0; width: 100%; }
  .band--red {
    top: 0; height: 448px;
    background: radial-gradient(ellipse at 85% 70%, var(--band-red) 0%, #a8342a 55%, var(--band-red-deep) 100%);
  }
  .band--white { top: 448px; height: 345px; background: var(--band-white); }
  .band--blue {
    top: 793px; height: 407px;
    background: radial-gradient(ellipse at 70% 30%, var(--band-blue) 0%, #2f4890 55%, var(--band-blue-deep) 100%);
  }
  .type-layer {
    position: absolute;
    inset: 0;
    width: 751px;
    height: 1200px;
    font-family: "Bebas Neue", "Oswald", sans-serif;
  }
  .title-red { fill: var(--title-red); }
  .title-blue { fill: var(--title-blue); }
  .author { fill: var(--author); }
  .star { fill: var(--star); }
  .visually-hidden {
    position: absolute; width: 1px; height: 1px; overflow: hidden;
    clip: rect(0 0 0 0); white-space: nowrap;
  }
</style>
</head>
<body>
  <main class="cover">
    <div class="band band--red"></div>
    <div class="band band--white"></div>
    <div class="band band--blue"></div>

    <h1 class="visually-hidden">The Orchard Below</h1>
    <p class="visually-hidden">Brenno Saltvik</p>

    <svg class="type-layer" viewBox="0 0 751 1200" aria-hidden="true">
      <defs>
        <polygon id="star" points="20,2 24.7,14.5 38,14.5 27.2,22.5 31.2,35.5 20,27.6 8.8,35.5 12.8,22.5 2,14.5 15.3,14.5"/>
      </defs>

      <g class="star" transform="translate(55 52)">
        <use href="#star" x="0"/><use href="#star" x="66.7"/><use href="#star" x="133.3"/>
        <use href="#star" x="200"/><use href="#star" x="266.7"/><use href="#star" x="333.3"/>
        <use href="#star" x="400"/><use href="#star" x="466.7"/><use href="#star" x="533.3"/>
        <use href="#star" x="600"/>
      </g>

      <text class="title-red" x="70" y="655" font-size="93" textLength="100" lengthAdjust="spacingAndGlyphs">THE</text>
      <text class="title-red" x="185" y="660" font-size="297" textLength="505" lengthAdjust="spacingAndGlyphs">ORCHARD</text>
      <text class="title-blue" x="70" y="790" font-size="174" textLength="620" lengthAdjust="spacing">BELOW</text>

      <text class="author" x="95" y="1035" font-size="79" textLength="585" lengthAdjust="spacing">BRENNO SALTVIK</text>

      <g class="star" transform="translate(68 1117)">
        <use href="#star" x="0"/><use href="#star" x="66.7"/><use href="#star" x="133.3"/>
        <use href="#star" x="200"/><use href="#star" x="266.7"/><use href="#star" x="333.3"/>
        <use href="#star" x="400"/><use href="#star" x="466.7"/><use href="#star" x="533.3"/>
        <use href="#star" x="600"/>
      </g>
    </svg>
  </main>
</body>
</html>
```